TOLMANNER GRILL CONCEPT

Tolmanner is a new kebab concept from Germany that we want to adapt to the market, we are in a new market. black and white as on the picture. it takes colors in adequation with the stickers. the packaging that will be personalized in the bag

Target Market(s)

students, executives, office worker

Industry/Entity Type

Fast Food Chain

Font styles to use
Serif
Script

Colors

Designer to choose colors to be used in the design.

Requirements
Must have
• - TOLMANNER GRILL LOGO - 87 Rue des Quenouilles, 75011 Paris - "Seit 1971"

```html
<!DOCTYPE html>
<html lang="en">
<head>
<meta charset="utf-8">
<title>Tolmanner Grill – Packaging Set</title>
<link rel="stylesheet" href="https://fonts.googleapis.com/css2?family=Josefin+Sans:wght@400&family=Oswald:wght@600&family=Didact+Gothic&display=swap">
<style>
  :root{
    --backdrop:#95a5a4;
    --orange:#f0921e;
    --orange-deep:#e88414;
    --kraft:#efa63a;
    --pattern-light:#f6e4cc;
    --ink:#111111;
    --paper:#ffffff;
  }
  *{box-sizing:border-box;margin:0;padding:0}
  html,body{width:1200px;height:1200px;overflow:hidden;background:var(--backdrop)}
  .canvas{position:relative;width:1200px;height:1200px}

  .badge{position:absolute;border-radius:50%;background:var(--ink);display:flex;align-items:center;justify-content:center;text-align:center}
  .badge-name{font-family:"Josefin Sans",sans-serif;font-weight:400;color:var(--paper);letter-spacing:.06em;line-height:1.15}

  .tagline{position:absolute;left:0;right:0;display:flex;align-items:center;gap:8px}
  .tagline .dots{flex:1;border-top:3px dotted var(--ink)}
  .tagline .since{font-family:"Oswald",sans-serif;font-weight:600;color:var(--ink);white-space:nowrap}
  .address{position:absolute;left:0;right:0;text-align:center;font-family:"Didact Gothic",sans-serif;color:var(--ink);white-space:nowrap}

  /* Bag */
  .bag-handle{position:absolute;left:774px;top:48px;width:262px;height:120px;border:26px solid var(--kraft);border-bottom:none}
  .bag{position:absolute;left:682px;top:152px;width:440px;height:604px;background:var(--orange)}
  .bag .pattern{position:absolute;inset:0 0 36px 0;background:var(--orange)}
  .bag .badge{left:148px;top:230px;width:144px;height:144px}
  .bag .badge-name{font-size:17px}
  .bag .tagline{top:562px;padding:0 2px}
  .bag .tagline .since{font-size:11px}
  .bag .address{top:584px;font-size:8px}

  /* Cup */
  .cup{position:absolute;left:356px;top:144px;width:260px;height:426px}

  /* Letterhead */
  .letterhead{position:absolute;left:98px;top:626px;width:358px;height:504px;background:var(--paper)}
  .letterhead .header-band{position:absolute;left:20px;right:22px;top:0;height:54px;background:var(--orange)}
  .letterhead .header-rule{position:absolute;left:20px;right:22px;top:56px;border-top:1px solid var(--orange)}
  .letterhead .badge{left:141px;top:15px;width:74px;height:74px}
  .letterhead .badge-name{font-size:8.5px}
  .letterhead .footer-strip{position:absolute;left:0;right:0;bottom:0;height:22px;background:var(--pattern-light)}
  .letterhead .footer-band{position:absolute;left:92px;width:172px;bottom:0;height:22px;background:var(--orange)}
  .letterhead .tagline{top:478px}
  .letterhead .tagline .dots{border-top-width:2px}
  .letterhead .tagline .since{font-size:6px}
  .letterhead .address{top:490px;font-size:5px}

  /* Napkin */
  .napkin{position:absolute;left:586px;top:816px;width:532px;height:304px;background:var(--paper)}
  .napkin .pattern{position:absolute;inset:0 0 44px 0;background:var(--pattern-light)}
  .napkin .badge{left:205px;top:77px;width:122px;height:122px}
  .napkin .badge-name{font-size:14px}
  .napkin .tagline{top:266px;padding:0 6px}
  .napkin .tagline .since{font-size:10px}
  .napkin .address{top:282px;font-size:8.5px}
</style>
</head>
<body>
<main class="canvas">

  <section class="carry-bag">
    <div class="bag-handle"></div>
    <div class="bag">
      <div class="pattern" role="img" aria-label="Hand-drawn white line doodle pattern of coffee cups, cheese, pizza slices, hot dogs and sweets on orange"></div>
      <div class="badge"><span class="badge-name">TOLMANNER<br>GRILL</span></div>
      <div class="tagline"><span class="dots"></span><span class="since">Since 1971</span><span class="dots"></span></div>
      <p class="address">87 Rue des Quenouilles, 75011 Paris</p>
    </div>
  </section>

  <svg class="cup" viewBox="0 0 260 426" xmlns="http://www.w3.org/2000/svg">
    <defs>
      <clipPath id="cup-body"><polygon points="20,60 240,60 206,426 56,426"/></clipPath>
    </defs>
    <g clip-path="url(#cup-body)">
      <rect x="0" y="60" width="260" height="366" fill="var(--paper)"/>
      <rect class="cup-pattern" x="0" y="108" width="260" height="280" fill="var(--orange)" role="img" aria-label="Orange doodle food pattern band"/>
      <rect x="0" y="60" width="260" height="48" fill="var(--pattern-light)" role="img" aria-label="Light doodle food pattern band"/>
      <rect x="0" y="388" width="260" height="38" fill="var(--pattern-light)" role="img" aria-label="Light doodle food pattern band"/>
    </g>
    <rect x="8" y="28" width="244" height="30" rx="8" fill="var(--ink)"/>
    <path d="M36 28 Q40 0 70 0 H190 Q220 0 224 28 Z" fill="var(--ink)"/>
    <circle cx="130" cy="244" r="58" fill="var(--ink)"/>
    <text x="130" y="240" text-anchor="middle" font-family="Josefin Sans, sans-serif" font-size="13" letter-spacing="0.8" fill="var(--paper)">TOLMANNER</text>
    <text x="130" y="257" text-anchor="middle" font-family="Josefin Sans, sans-serif" font-size="13" letter-spacing="0.8" fill="var(--paper)">GRILL</text>
    <line x1="46" y1="358" x2="106" y2="358" stroke="var(--ink)" stroke-width="2.5" stroke-dasharray="2 3"/>
    <line x1="154" y1="358" x2="214" y2="358" stroke="var(--ink)" stroke-width="2.5" stroke-dasharray="2 3"/>
    <text x="130" y="362" text-anchor="middle" font-family="Oswald, sans-serif" font-weight="600" font-size="10" fill="var(--ink)">Since 1971</text>
    <text x="130" y="377" text-anchor="middle" font-family="Didact Gothic, sans-serif" font-size="7" fill="var(--ink)">87 Rue des Quenouilles, 75011 Paris</text>
  </svg>

  <section class="letterhead">
    <div class="header-band" role="img" aria-label="Orange doodle food pattern header band"></div>
    <div class="header-rule"></div>
    <div class="badge"><span class="badge-name">TOLMANNER<br>GRILL</span></div>
    <div class="footer-strip" role="img" aria-label="Light doodle food pattern footer strip"></div>
    <div class="footer-band"></div>
    <div class="tagline"><span class="dots"></span><span class="since">Since 1971</span><span class="dots"></span></div>
    <p class="address">87 Rue des Quenouilles, 75011 Paris</p>
  </section>

  <section class="napkin">
    <div class="pattern" role="img" aria-label="Faint orange line doodle pattern of coffee, cheese, pizza and hot dogs on white"></div>
    <div class="badge"><span class="badge-name">TOLMANNER<br>GRILL</span></div>
    <div class="tagline"><span class="dots"></span><span class="since">Since 1971</span><span class="dots"></span></div>
    <p class="address">87 Rue des Quenouilles, 75011 Paris</p>
  </section>

</main>
</body>
</html>
```